Corvell Advisory

Business Development Consulting Firm

Target Market(s)

Federal Government, 8(a) companies, Small Businesses

Industry/Entity Type

Private Sector, US Government

Contact Information for Business Card

8(a) Program Capture, Business Development, Industry Trends & Analysis, Strategic Teaming, Cyber Solutions

Colors

Designer to choose colors to be used in the design.

```html
<!DOCTYPE html>
<html lang="en">
<head>
<meta charset="UTF-8">
<title>Corvell Advisory — Business Cards</title>
<link rel="stylesheet" href="https://fonts.googleapis.com/css2?family=Michroma&family=Montserrat:wght@400;500&family=Oswald:wght@300;400&family=Saira:wght@500&display=swap">
<style>
  :root {
    --page-bg: #d8d5d0;
    --front-bg: #040a15;
    --back-bg: #111214;
    --accent: #1ba6e4;
    --beam: rgba(38, 128, 175, 0.55);
    --map-blue-1: #0f4466;
    --map-blue-2: #071a2c;
    --map-grey-1: #3a3b3d;
    --map-grey-2: #18191b;
    --text-light: #f2f4f6;
    --text-muted: #a9adb2;
    --panel: #1d2023;
  }
  * { box-sizing: border-box; margin: 0; padding: 0; }
  html, body { width: 1200px; height: 900px; overflow: hidden; }
  body { background: var(--page-bg); position: relative; font-family: "Montserrat", sans-serif; }

  .card {
    position: absolute; left: 285px; width: 630px; height: 360px;
    overflow: hidden; border-radius: 4px;
    box-shadow: 0 12px 30px rgba(0,0,0,0.28);
  }
  .card--front { top: 48px; background: var(--front-bg); }
  .card--back { top: 492px; background: var(--back-bg); }

  .map-area { position: absolute; }
  .card--front .map-area {
    left: 150px; top: 20px; width: 470px; height: 330px;
    background: radial-gradient(ellipse at 55% 45%, var(--map-blue-1) 0%, var(--map-blue-2) 60%, transparent 80%);
    opacity: 0.9;
  }
  .card--back .map-area {
    left: 0; top: 0; width: 300px; height: 360px;
    background: radial-gradient(ellipse at 45% 40%, var(--map-grey-1) 0%, var(--map-grey-2) 65%, transparent 85%);
  }

  .shapes { position: absolute; inset: 0; width: 100%; height: 100%; }

  .brand-name {
    position: absolute; font-family: "Saira", sans-serif; font-weight: 500;
    letter-spacing: 0.14em; text-transform: uppercase;
  }
  .card--front .brand-name { left: 38px; top: 40px; font-size: 21px; color: var(--text-light); }
  .card--back .brand-name { left: 40px; bottom: 44px; font-size: 15px; color: var(--accent); }

  .services {
    position: absolute; left: 38px; top: 100px; width: 220px; padding: 16px 20px;
    background: rgba(40, 112, 145, 0.32);
  }
  .services li {
    list-style: none; font-family: "Oswald", sans-serif; font-weight: 300;
    font-size: 14px; letter-spacing: 0.04em; line-height: 1.55;
    color: var(--text-light); text-transform: uppercase;
  }
  .services .bracket { position: absolute; width: 16px; height: 16px; border: 0 solid var(--accent); }
  .bracket--tl { left: -6px; top: -6px; border-left-width: 2px !important; border-top-width: 2px !important; }
  .bracket--br { right: -6px; bottom: -6px; border-right-width: 2px !important; border-bottom-width: 2px !important; }
  .bracket--bl { left: -6px; bottom: -6px; border-left-width: 2px !important; border-bottom-width: 2px !important; }

  .person { position: absolute; right: 48px; top: 58px; text-align: right; }
  .person__name {
    font-family: "Michroma", sans-serif; font-size: 17px; color: var(--accent);
    letter-spacing: 0.06em; text-transform: uppercase;
  }
  .person__title {
    margin-top: 6px; font-size: 10px; color: var(--text-muted);
    letter-spacing: 0.22em; text-transform: uppercase;
  }

  .contacts { position: absolute; right: 78px; top: 158px; text-align: right; color: var(--text-light); font-size: 11.5px; line-height: 1.45; }
  .contacts p { margin-bottom: 7px; }

  .icon-rail {
    position: absolute; right: 0; top: 150px; width: 44px; height: 150px;
    background: var(--panel); border-radius: 14px 0 0 14px;
    display: flex; flex-direction: column; justify-content: space-around; align-items: center;
    padding: 8px 0;
  }
  .icon-rail svg { width: 16px; height: 16px; fill: none; stroke: var(--accent); stroke-width: 1.4; stroke-linecap: round; stroke-linejoin: round; }
</style>
</head>
<body>

<section class="card card--front" aria-label="Card front">
  <div class="map-area" role="img" aria-label="World map rendered in a fine dotted blue texture"></div>
  <svg class="shapes" viewBox="0 0 630 360" aria-hidden="true">
    <polygon points="150,360 330,205 395,222 255,360" fill="var(--beam)"/>
    <polygon points="385,360 455,112 520,124 470,360" fill="var(--beam)"/>
  </svg>
  <div class="brand-name">Corvell Advisory</div>
  <ul class="services">
    <span class="bracket bracket--tl"></span>
    <span class="bracket bracket--bl"></span>
    <span class="bracket bracket--br"></span>
    <li>Program Capture</li>
    <li>Business Development</li>
    <li>Industry Trends &amp; Analysis</li>
    <li>Strategic Teaming</li>
  </ul>
</section>

<section class="card card--back" aria-label="Card back">
  <div class="map-area" role="img" aria-label="World map rendered in a fine dotted grey texture"></div>
  <svg class="shapes" viewBox="0 0 630 360" aria-hidden="true">
    <polygon points="0,250 150,0 240,0 60,360 0,360" fill="rgba(255,255,255,0.035)"/>
    <polygon points="160,360 250,0 330,0 255,360" fill="rgba(255,255,255,0.045)"/>
    <line x1="330" y1="0" x2="255" y2="360" stroke="rgba(255,255,255,0.12)" stroke-width="2"/>
  </svg>
  <div class="brand-name">Corvell Advisory</div>

  <div class="person">
    <h1 class="person__name">Dana Whitfield</h1>
    <p class="person__title">Position/Title</p>
  </div>

  <div class="contacts">
    <p>(555) 318-4426</p>
    <p>dana.w@corvelladvisory.com</p>
    <p>4820 Harbor Point Suite 210<br>Eastvale, Maryland</p>
    <p>www.corvelladvisory.com</p>
  </div>

  <div class="icon-rail" aria-hidden="true">
    <svg viewBox="0 0 16 16"><path d="M4 2l2.5 3-1.5 1.5a8 8 0 0 0 4.5 4.5L11 9.5l3 2.5-1.5 2A10 10 0 0 1 2 3.5z"/></svg>
    <svg viewBox="0 0 16 16"><rect x="2" y="4" width="12" height="9" rx="1.5"/><path d="M2.5 5l5.5 4 5.5-4"/></svg>
    <svg viewBox="0 0 16 16"><circle cx="8" cy="8" r="6"/><circle cx="8" cy="8" r="2"/></svg>
    <svg viewBox="0 0 16 16"><circle cx="8" cy="8" r="6"/><ellipse cx="8" cy="8" rx="2.6" ry="6"/><path d="M2 8h12"/></svg>
  </div>
</section>

</body>
</html>
```